Business cards to launch an education platform

Hi,
I am looking at having new business cards designed.
I am a startup, developing a web platform for schools and university, the education world. It's an online assessment system.
I would like a card that looks classy, and that is using the colors and the font of my logo.

I have attached:
1) my logo
2) A business card that I have designed quickly so you can have all the information required in the card, but I really don't like it.
3) The font that I am using (Lato Regular) to design my web platform
4) Some screenshots of my web platform so you can have a look at the style that I have.

Target Market(s)

Major market: Education system: Schools and university
Minor markets: Business in general

Industry/Entity Type

Business

Contact Information for Business Card

Lydia Marsh
Director

M: 0437 681 902
E: lydia.marsh@copperLeafSystems.com.au

Requirements
Must have
• The colors of my logo

```html
<!DOCTYPE html>
<html lang="en">
<head>
<meta charset="utf-8">
<title>Copper Leaf Systems – Business Card</title>
<link rel="stylesheet" href="https://fonts.googleapis.com/css2?family=Lato:wght@400;700&display=swap">
<style>
  :root {
    --page-bg: #e4e2df;
    --card-bg: #f4f5f7;
    --navy: #1d3557;
    --ink: #2f3f52;
    --sky: #2a8fc9;
    --teal: #2fa3b5;
    --blue-deep: #1b4f8f;
    --blue-mid: #2a6fb3;
  }
  * { margin: 0; padding: 0; box-sizing: border-box; }
  html, body {
    width: 1200px;
    height: 970px;
    overflow: hidden;
    background: var(--page-bg);
    font-family: "Lato", sans-serif;
  }
  .business-card {
    position: absolute;
    left: 80px;
    top: 190px;
    width: 1040px;
    height: 590px;
    background: var(--card-bg);
    box-shadow: 0 10px 30px rgba(0,0,0,0.18);
    overflow: hidden;
  }
  .card-art {
    position: absolute;
    inset: 0;
  }
  .brand {
    position: absolute;
    left: 65px;
    top: 100px;
    display: flex;
    align-items: center;
    gap: 28px;
  }
  .brand-mark {
    width: 110px;
    height: 110px;
    background: var(--blue-mid);
  }
  .brand-name {
    color: var(--navy);
    font-weight: 400;
    line-height: 1;
  }
  .brand-name .line-main {
    display: block;
    font-size: 58px;
    letter-spacing: 5px;
  }
  .brand-name .line-sub {
    display: block;
    font-size: 40px;
    letter-spacing: 4px;
    margin-top: 14px;
  }
  .holder {
    position: absolute;
    left: 65px;
    top: 340px;
  }
  .holder-name {
    font-size: 38px;
    font-weight: 700;
    color: var(--ink);
    line-height: 1.1;
  }
  .holder-role {
    font-size: 26px;
    color: var(--sky);
    line-height: 1.2;
  }
  .contact-list {
    position: absolute;
    left: 65px;
    top: 455px;
    list-style: none;
  }
  .contact-item {
    display: flex;
    align-items: center;
    gap: 12px;
    font-size: 28px;
    color: var(--ink);
    line-height: 36px;
  }
  .contact-icon {
    width: 30px;
    height: 30px;
    flex: none;
  }
</style>
</head>
<body>
  <div class="business-card">
    <svg class="card-art" viewBox="0 0 1040 590" width="1040" height="590" aria-hidden="true">
      <defs>
        <linearGradient id="band-fill" x1="0" y1="0" x2="1" y2="1">
          <stop offset="0" stop-color="#2d7cc2"/>
          <stop offset="0.5" stop-color="#1f62a6"/>
          <stop offset="1" stop-color="#174a86"/>
        </linearGradient>
      </defs>
      <path class="blue-band" d="M650,0 C860,70 995,240 955,400 C932,490 850,560 760,590 L1040,590 L1040,0 Z" fill="url(#band-fill)"/>
      <path class="teal-arc" d="M380,0 C720,40 955,210 925,390 C908,480 830,560 745,590" fill="none" stroke="var(--teal)" stroke-width="9"/>
    </svg>

    <div class="brand">
      <div class="brand-mark"></div>
      <div class="brand-name">
        <span class="line-main">COPPER LEAF</span>
        <span class="line-sub">Systems</span>
      </div>
    </div>

    <div class="holder">
      <p class="holder-name">Lydia Marsh</p>
      <p class="holder-role">Director</p>
    </div>

    <ul class="contact-list">
      <li class="contact-item">
        <svg class="contact-icon" viewBox="0 0 30 30" aria-hidden="true">
          <rect x="0" y="0" width="30" height="30" fill="var(--blue-mid)"/>
          <rect x="10" y="5" width="10" height="20" rx="2" fill="none" stroke="#fff" stroke-width="1.8"/>
          <rect x="12" y="8" width="6" height="6" fill="#fff"/>
        </svg>
        <span>0437 681 902</span>
      </li>
      <li class="contact-item">
        <svg class="contact-icon" viewBox="0 0 30 30" aria-hidden="true">
          <rect x="0" y="0" width="30" height="30" fill="var(--blue-mid)"/>
          <rect x="5" y="8" width="20" height="14" fill="none" stroke="#fff" stroke-width="1.8"/>
          <path d="M5,8 L15,16 L25,8" fill="none" stroke="#fff" stroke-width="1.8"/>
        </svg>
        <span>lydia.marsh@copperLeafSystems.com.au</span>
      </li>
    </ul>
  </div>
</body>
</html>
```